E-Liquid Bottle Labels

We are looking to redesign the label on our e-cigarette juice bottles.

We are trying to brand our company "Copper Lantern Mists" by using the Copper Lantern portion of our logo prominently on our current labels. The goal is to have customers know our product when they just see the diamond and not need to read our name to know its a Copper Lantern Premium E-Liquid.

We carry 50 different flavors that each come in 5 sizes. Additionally each size comes in 4 different levels of nicotine strength (0 mg, 6 mg, 12 mg, and 18 mg) Due to label cost runs we need to put each nicotine strengths on the label with a "checkbox" system next to them so we can manually mark the correct mg strength on each bottle after applying the label.

The labels should include the following:

1- The Copper Lantern in our logo as the focal point
2- The name "Copper Lantern Mists" in our logo font Trajan Bold Pro
3- The words "Premium E-Liquid"
4- The name of the Premium E-Liquid. We have 50 flavors (please see attached flavor grid with the shortest name being "Kiwi" and the longest being "Banana Cream Menthol")
5- The following text "Caution: This product contains Nicotine. Keep out of the reach of children and pets. Do not drink. Not for sale to minors.
6- The following text "Ingredients: Propylene Glycol (USP),Glycerin (USP), L-Nicotine, FEMA/GRAS approved Natural and Artificial Flavorings. All ingredients are FDA approved for human consumption.
7- Some type of checkbox set up to mark whether the juice has "0 mg", "6 mg", "12 mg", or "18 mg" of nicotine

Although the same design will be used across all bottle sizes. We will need to make sure that the design gets a finished version in all 5 sizes.

There are 5 sizes of labels:

1- 15 ml squeeze is 2 3/4" wide x 1 5/8" high
2- 30 ml squeeze is 3 1/2" wide x 1 3/4" high
3- 15 ml glass is 3" wide x 1 1/4" high
4- 30 ml glass is 3 5/8" wide x 1 1/2" high
5- 60 ml glass is 4 5/8" wide x 1 3/4" high

Colors
0455a3
3176b5
85acd3
ceddec
0692cd
33a6d7
85cae6
cee9f5

```html
<!DOCTYPE html>
<html lang="en">
<head>
<meta charset="utf-8">
<title>Copper Lantern Mists – French Vanilla Label</title>
<link rel="stylesheet" href="https://fonts.googleapis.com/css2?family=Cinzel:wght@400;600;700&family=Noto+Sans:wght@400;700&display=swap">
<style>
  :root{
    --navy:#0455a3;
    --mid-blue:#3176b5;
    --soft-blue:#85acd3;
    --pale-blue:#ceddec;
    --bright-blue:#0692cd;
    --sky:#33a6d7;
    --light-sky:#85cae6;
    --mist:#cee9f5;
    --stone-dark:#bdb6b6;
    --stone:#d6d0cf;
    --stone-light:#ece8e6;
    --ink:#1d1d1d;
    --white:#ffffff;
  }
  *{box-sizing:border-box;margin:0;padding:0}
  html,body{width:1200px;height:1200px;overflow:hidden;background:#ffffff}
  .canvas{position:relative;width:1200px;height:1200px}
  .label{
    position:absolute;left:40px;top:388px;width:1120px;height:423px;overflow:hidden;
    font-family:"Noto Sans",Arial,sans-serif;color:var(--ink);
  }
  .label__facets{
    position:absolute;inset:0 0 107px 0;
    background:
      linear-gradient(115deg,rgba(255,255,255,0) 55%,rgba(255,255,255,.45) 80%),
      linear-gradient(100deg,var(--stone) 0%,var(--stone-dark) 28%,var(--stone-light) 48%,var(--stone) 68%,var(--stone-light) 100%);
  }
  .label__band{
    position:absolute;left:0;right:0;bottom:0;height:107px;
    background:linear-gradient(100deg,var(--navy) 0%,var(--mid-blue) 22%,var(--sky) 48%,var(--bright-blue) 62%,var(--navy) 78%,var(--light-sky) 100%);
  }
  .flavor-tab{
    position:absolute;left:420px;top:0;width:258px;height:43px;
    background:var(--mid-blue);color:var(--white);
    font-family:"Cinzel",serif;font-weight:600;font-size:25px;
    display:flex;align-items:center;justify-content:center;letter-spacing:.5px;
  }
  .product-line{
    position:absolute;left:0;right:0;top:66px;text-align:center;
    font-family:"Cinzel",serif;font-weight:600;font-size:27px;color:var(--navy);letter-spacing:.5px;
  }
  .brand-mark{
    position:absolute;left:417px;top:120px;width:286px;height:180px;
    display:flex;flex-direction:column;align-items:center;justify-content:center;gap:14px;
  }
  .brand-mark__dot{width:46px;height:46px;border-radius:50%;background:var(--navy)}
  .brand-mark__name{font-family:"Cinzel",serif;font-weight:700;font-size:34px;color:var(--navy);text-align:center;line-height:1.1}
  .panel{position:absolute;top:86px;width:210px;font-size:15.5px;line-height:24.5px}
  .panel__title{font-weight:700;font-size:15.5px;margin-bottom:14px}
  .panel--ingredients{left:34px}
  .panel--caution{left:873px;width:220px}
  .strengths{margin-top:12px}
  .strengths__title{font-weight:700;font-size:12.5px;line-height:16px;margin-bottom:5px}
  .strengths__list{display:flex;gap:10px;list-style:none}
  .strength{position:relative;width:30px;height:30px;display:flex;align-items:center;justify-content:center;font-size:13.5px}
  .strength svg{position:absolute;inset:0}
  .brand-name{
    position:absolute;left:0;right:0;bottom:22px;text-align:center;
    font-family:"Cinzel",serif;font-weight:700;font-size:44px;color:var(--white);letter-spacing:1px;
  }
</style>
</head>
<body>
<main class="canvas">
  <section class="label">
    <div class="label__facets" role="img" aria-label="Faceted low-poly background in soft greys"></div>
    <div class="label__band" role="img" aria-label="Faceted low-poly band in shades of blue"></div>

    <div class="flavor-tab">French Vanilla</div>
    <div class="product-line">Premium E-Liquid</div>

    <div class="brand-mark">
      <span class="brand-mark__dot"></span>
      <span class="brand-mark__name">Copper Lantern</span>
    </div>

    <div class="panel panel--ingredients">
      <p class="panel__title">INGREDIENTS:</p>
      <p>Propylene Glycol (USP), Glycerin (USP), L-Nicotine, FEMA/GRAS Approved Natural / Artificial Flavoring. All ingredients are FDA approved for human consumption.</p>
    </div>

    <div class="panel panel--caution">
      <p class="panel__title">CAUTION :</p>
      <p>This product contains nicotine. Keep out of reach of children and pets. Do not drink.<br>Not for sale to minors.</p>
      <div class="strengths">
        <p class="strengths__title">Nicotines in miligram:</p>
        <ul class="strengths__list">
          <li class="strength"><svg viewBox="0 0 30 30"><circle cx="15" cy="15" r="13" fill="#fff" stroke="#1d1d1d" stroke-width="2.5"/></svg><span style="position:relative">0</span></li>
          <li class="strength"><svg viewBox="0 0 30 30"><circle cx="15" cy="15" r="13" fill="#fff" stroke="#1d1d1d" stroke-width="2.5"/><path d="M15 2 A13 13 0 0 1 26 22" fill="none" stroke="#33a6d7" stroke-width="2.5"/></svg><span style="position:relative">6</span></li>
          <li class="strength"><svg viewBox="0 0 30 30"><circle cx="15" cy="15" r="13" fill="#fff" stroke="#1d1d1d" stroke-width="2.5"/><path d="M15 2 A13 13 0 0 1 15 28" fill="none" stroke="#33a6d7" stroke-width="2.5"/></svg><span style="position:relative">12</span></li>
          <li class="strength"><svg viewBox="0 0 30 30"><circle cx="15" cy="15" r="13" fill="#fff" stroke="#1d1d1d" stroke-width="2.5"/><path d="M15 2 A13 13 0 1 1 4 8" fill="none" stroke="#33a6d7" stroke-width="2.5"/></svg><span style="position:relative">18</span></li>
        </ul>
      </div>
    </div>

    <div class="brand-name">Copper Lantern Mists</div>
  </section>
</main>
</body>
</html>
```